Interior designer needs a power point template design

I need a template PowerPoint design for my client presentations. The presentations I prepare for my clients usually include the furniture project, the detail of the selected furniture, and the costs. There are a lot of images I insert. What I need is to have a template that I can use for all my presentations, where from time to time I will insert the specific images and descriptions I want to insert. What will always be the same will be the cover, the colors, the font, and the design of the internal sections.
I already have my logo that I would like to insert on each page of the presentation (in small size).
In summary, I need:
- basic template design
- cover with an image chosen by Picsmeadow photo
- design an internal section/chapter
- internal page design.

I like the clolors of pink and brown <8please see image attached)
Images (will come from Picsmeadow photo)
● entrance/hall
● living room
● dining room
● Bathroom
● Closet
● Kids room
● Master bedroom
● Master bathroom
● Kitchen
● Office
● Laundry
● Balcony or Terrace

Target Market(s)

Customers (both residential and commercial projects)

Industry/Entity Type

interior design

Font styles to use
Other font styles liked:
• I like courier new

Requirements
Must have
• beautiful design
Should not have
• animations

```html
<!DOCTYPE html>
<html lang="en">
<head>
<meta charset="utf-8">
<title>Stanza Chiara – Presentation Template</title>
<link rel="stylesheet" href="https://fonts.googleapis.com/css2?family=Antonio:wght@100;200;300&family=Montserrat:wght@400;500&display=swap">
<style>
  :root{
    --wine:#7d2117;
    --wine-soft:#8a2c21;
    --wine-deep:#6e1c13;
    --rose:#f2c7b8;
    --rose-line:#e7b3a3;
    --coral:#d8724c;
    --white:#ffffff;
    --paper:#f3f3f3;
    --board:#b9b9b9;
    --sky-top:#e4e7eb;
    --sky-bottom:#c8ccd1;
    --ink:#5b6068;
    --display:"Antonio", "Arial Narrow", sans-serif;
    --body:"Montserrat", Arial, sans-serif;
  }
  *{margin:0;padding:0;box-sizing:border-box}
  html,body{width:681px;height:1200px;overflow:hidden}
  body{position:relative;background:var(--board);font-family:var(--body)}

  /* hero area */
  .hero{position:absolute;left:0;top:0;width:681px;height:411px;
    background:linear-gradient(180deg,var(--sky-top) 0%,var(--sky-bottom) 100%)}
  .hero__cover{position:absolute;left:78px;top:92px;transform:scale(1.15);transform-origin:0 0;
    box-shadow:0 10px 24px rgba(0,0,0,.18)}
  .hero__brand{position:absolute;left:548px;top:40px;width:100px;text-align:center}
  .hero__brand svg{display:block;margin:0 auto}
  .hero__brand .brand__name{color:var(--ink);font-size:26px;line-height:1;margin-top:12px;letter-spacing:2px}

  /* grid of slides */
  .slide{position:absolute;width:319px;height:179px;overflow:hidden;background:var(--white)}
  .col-a{left:16px}.col-b{left:346px}
  .row-1{top:430px}.row-2{top:620px}.row-3{top:810px}.row-4{top:1001px}

  .fill{position:absolute}
  .wine{background:var(--wine)}
  .room-bg{background:linear-gradient(135deg,#93382b 0%,#82291e 55%,#772217 100%)}

  .photo{position:absolute;border:1px solid #ddd}
  .photo--bedroom{background:linear-gradient(160deg,#efece8 0%,#d9d2c9 50%,#b9a897 100%)}
  .photo--bath{background:linear-gradient(160deg,#f4f4f2 0%,#e3e1dc 55%,#c9b49a 100%)}
  .photo--dining1{background:linear-gradient(170deg,#e9ede8 0%,#b8c2b1 45%,#4a4a4c 100%)}
  .photo--dining2{background:linear-gradient(170deg,#7d8585 0%,#a9a39b 50%,#c69b6b 100%)}
  .photo--kitchen1{background:linear-gradient(160deg,#f1f1ef 0%,#dcd8d2 55%,#b89f84 100%)}
  .photo--kitchen2{background:linear-gradient(160deg,#ecebe8 0%,#d0c6b8 55%,#a88a6a 100%)}
  .photo--balcony1{background:linear-gradient(160deg,#ece9e4 0%,#8a7d6c 55%,#a07a3e 100%)}
  .photo--balcony2{background:linear-gradient(160deg,#f0efec 0%,#8b8c8f 55%,#d6a72a 100%)}

  /* brand lockup */
  .brand{position:absolute;text-align:center}
  .brand svg{display:block;margin:0 auto}
  .brand__name{font-family:var(--display);font-weight:200;color:var(--rose);
    text-transform:uppercase;letter-spacing:1px;line-height:1}
  .brand--cover{left:38px;top:46px;width:56px}
  .brand--cover .brand__name{font-size:14px;margin-top:6px}
  .brand--mini{width:40px}
  .brand--mini .brand__name{font-size:8px;margin-top:3px;opacity:.8}

  /* cover text */
  .cover__kicker{position:absolute;left:150px;top:46px;font-family:var(--display);font-weight:200;
    font-size:11px;color:var(--rose);letter-spacing:.3px}
  .cover__title{position:absolute;left:150px;top:60px;font-family:var(--display);font-weight:200;
    font-size:21px;color:var(--rose);letter-spacing:.4px}
  .cover__subtitle{position:absolute;left:150px;top:92px;font-family:var(--display);font-weight:200;
    font-size:6.5px;color:var(--rose-line);letter-spacing:.3px}
  .cover__date{position:absolute;left:151px;top:112px;width:72px;height:10px;border-radius:1.5px;
    background:var(--coral);color:var(--rose);font-family:var(--display);font-weight:200;
    font-size:4.6px;line-height:10px;text-align:center;letter-spacing:.3px}
  .cover__rule{position:absolute;height:1px;background:rgba(242,199,184,.25)}
  .footer-band{position:absolute;left:0;bottom:0;width:100%;height:11px;background:var(--paper);
    font-size:4.2px;line-height:11px;text-align:center;color:#6a6a6a;letter-spacing:.2px}

  /* section text */
  .section__title{font-family:var(--display);font-weight:200;color:var(--rose);font-size:17px;
    letter-spacing:.4px;line-height:1}
  .section__text{font-size:4.6px;color:var(--rose);line-height:1.25;margin-top:5px}
  .section__block{position:absolute;text-align:center}

  /* page bar */
  .page-bar{position:absolute;left:8px;right:0;top:165px;height:4px;background:var(--coral);
    display:flex;justify-content:space-between;align-items:center;padding:0 6px 0 3px;
    font-size:2.6px;color:var(--white)}
  .page-bar__num{display:flex;gap:6px}
  .page-bar__num::before{content:"";width:.5px;height:3px;background:var(--white)}

  /* contact */
  .contact__kicker{position:absolute;left:150px;top:49px;font-family:var(--display);font-weight:200;
    font-size:12px;color:var(--rose)}
  .contact__name{position:absolute;left:150px;top:64px;font-family:var(--display);font-weight:200;
    font-size:21px;color:var(--rose);letter-spacing:.3px}
  .contact__address{position:absolute;left:150px;top:93px;font-family:var(--display);font-weight:300;
    font-size:6.5px;color:var(--rose)}
  .contact__list{position:absolute;left:150px;top:105px;list-style:none}
  .contact__list li{display:flex;align-items:center;gap:5px;height:9.3px;font-size:4.8px;color:var(--rose)}
  .contact__list svg{width:5px;height:5px}
</style>
</head>
<body>

<section class="hero">
  <!-- flat cover slide -->
  <article class="slide hero__cover">
    <div class="fill room-bg" style="inset:0" role="img" aria-label="Dining room with chairs and bookshelf, tinted in wine red"></div>
    <div class="brand brand--cover">
      <svg width="44" height="44" viewBox="0 0 44 44"><circle cx="22" cy="22" r="21" fill="none" stroke="var(--rose)" stroke-width=".6"/></svg>
      <div class="brand__name">Stanza<br>Chiara</div>
    </div>
    <div class="cover__kicker">STANZA CHIARA</div>
    <div class="cover__title">PRESENTATION TITLE</div>
    <div class="cover__subtitle">SUBTITLE OF PRESENTATION GOES HERE!</div>
    <div class="cover__date">FRIDAY, APRIL 15, 2022</div>
    <div class="footer-band">© 2022 STANZA CHIARA, All rights reserved.</div>
  </article>

  <div class="hero__brand">
    <svg width="72" height="72" viewBox="0 0 72 72"><circle cx="36" cy="36" r="35" fill="none" stroke="var(--ink)" stroke-width=".8"/></svg>
    <div class="brand__name">STANZA CHIARA</div>
  </div>
</section>

<!-- cover with photo -->
<article class="slide col-a row-1">
  <div class="fill room-bg" style="inset:0" role="img" aria-label="Dining room with chairs and bookshelf, tinted in wine red"></div>
  <div class="brand brand--cover">
    <svg width="44" height="44" viewBox="0 0 44 44"><circle cx="22" cy="22" r="21" fill="none" stroke="var(--rose)" stroke-width=".6"/></svg>
    <div class="brand__name">Stanza<br>Chiara</div>
  </div>
  <div class="cover__kicker">STANZA CHIARA</div>
  <div class="cover__title">PRESENTATION TITLE</div>
  <div class="cover__subtitle">SUBTITLE OF PRESENTATION GOES HERE!</div>
  <div class="cover__date">FRIDAY, APRIL 15, 2022</div>
  <div class="footer-band">© 2022 STANZA CHIARA, All rights reserved.</div>
</article>

<!-- cover plain -->
<article class="slide col-b row-1">
  <div class="fill wine" style="inset:0"></div>
  <div class="cover__rule" style="left:100px;top:86px;width:50px"></div>
  <div class="cover__rule" style="left:115px;top:42px;width:1px;height:80px"></div>
  <div class="brand brand--cover">
    <svg width="44" height="44" viewBox="0 0 44 44"><circle cx="22" cy="22" r="21" fill="none" stroke="var(--rose)" stroke-width=".6"/></svg>
    <div class="brand__name">Stanza<br>Chiara</div>
  </div>
  <div class="cover__kicker">STANZA CHIARA</div>
  <div class="cover__title">PRESENTATION TITLE</div>
  <div class="cover__subtitle">SUBTITLE OF PRESENTATION GOES HERE!</div>
  <div class="cover__date">FRIDAY, APRIL 15, 2022</div>
  <div class="footer-band">© 2022 STANZA CHIARA, All rights reserved.</div>
</article>

<!-- bedroom -->
<article class="slide col-a row-2">
  <div class="fill room-bg" style="left:0;top:0;width:160px;height:179px" role="img" aria-label="Bedroom interior, tinted in wine red"></div>
  <div class="photo photo--bedroom" style="left:132px;top:8px;width:180px;height:149px" role="img" aria-label="Bright bedroom with upholstered bed, chandelier and barn door"></div>
  <div class="brand brand--mini" style="left:63px;top:35px">
    <svg width="26" height="26" viewBox="0 0 26 26"><circle cx="13" cy="13" r="12.5" fill="none" stroke="var(--rose)" stroke-width=".5" opacity=".8"/></svg>
    <div class="brand__name">Stanza<br>Chiara</div>
  </div>
  <div class="section__block" style="left:12px;top:99px;width:108px">
    <div class="section__title">BEDROOM</div>
    <div class="section__text">Lorem ipsum dolor sit amet, consectetur adipiscing elit. Vivamus eu dui ex.</div>
  </div>
  <div class="page-bar"><span>© 2022 STANZA CHIARA, All rights reserved.</span><span class="page-bar__num">3</span></div>
</article>

<!-- bathroom -->
<article class="slide col-b row-2">
  <div class="fill room-bg" style="left:160px;top:0;width:159px;height:179px" role="img" aria-label="Bathroom interior, tinted in wine red"></div>
  <div class="photo photo--bath" style="left:8px;top:8px;width:179px;height:149px" role="img" aria-label="White bathroom with freestanding tub, shelves and wood floor"></div>
  <div class="brand brand--mini" style="left:239px;top:35px">
    <svg width="26" height="26" viewBox="0 0 26 26"><circle cx="13" cy="13" r="12.5" fill="none" stroke="var(--rose)" stroke-width=".5" opacity=".8"/></svg>
    <div class="brand__name">Stanza<br>Chiara</div>
  </div>
  <div class="section__block" style="left:200px;top:99px;width:104px">
    <div class="section__title">BATHROOM</div>
    <div class="section__text">Lorem ipsum dolor sit amet, consectetur adipiscing elit. Vivamus eu dui ex.</div>
  </div>
  <div class="page-bar"><span>© 2022 STANZA CHIARA, All rights reserved.</span><span class="page-bar__num">4</span></div>
</article>

<!-- dining room -->
<article class="slide col-a row-3">
  <div class="fill room-bg" style="left:0;top:0;width:319px;height:89px" role="img" aria-label="Dining room interior, tinted in wine red"></div>
  <div class="brand brand--mini" style="left:16px;top:22px">
    <svg width="26" height="26" viewBox="0 0 26 26"><circle cx="13" cy="13" r="12.5" fill="none" stroke="var(--rose)" stroke-width=".5" opacity=".8"/></svg>
    <div class="brand__name">Stanza<br>Chiara</div>
  </div>
  <div style="position:absolute;left:73px;top:29px;width:230px">
    <div class="section__title">DINING ROOM</div>
    <div class="section__text" style="margin-top:4px">Lorem ipsum dolor sit amet, consectetur adipiscing elit. Vivamus eu dui ex. Curabitur dapibus dignissim dui, in molestie metus feugiat sed. Praesent aliquet lorem ex, eu dapibus odio varius.</div>
  </div>
  <div class="photo photo--dining1" style="left:8px;top:97px;width:149px;height:58px" role="img" aria-label="Dining table with black chairs by large windows"></div>
  <div class="photo photo--dining2" style="left:162px;top:97px;width:150px;height:58px" role="img" aria-label="Dining table with grey chairs, tulips and white bookshelf"></div>
  <div class="page-bar"><span>© 2022 STANZA CHIARA, All rights reserved.</span><span class="page-bar__num">5</span></div>
</article>

<!-- kitchen -->
<article class="slide col-b row-3">
  <div class="fill room-bg" style="left:0;top:0;width:160px;height:179px" role="img" aria-label="Kitchen interior, tinted in wine red"></div>
  <div class="photo photo--kitchen1" style="left:133px;top:8px;width:179px;height:70px" role="img" aria-label="White kitchen island with bar stools and pendant lamps"></div>
  <div class="photo photo--kitchen2" style="left:133px;top:85px;width:179px;height:70px" role="img" aria-label="Modern kitchen with cabinets and wooden table"></div>
  <div class="brand brand--mini" style="left:47px;top:36px">
    <svg width="26" height="26" viewBox="0 0 26 26"><circle cx="13" cy="13" r="12.5" fill="none" stroke="var(--rose)" stroke-width=".5" opacity=".8"/></svg>
    <div class="brand__name">Stanza<br>Chiara</div>
  </div>
  <div class="section__block" style="left:14px;top:99px;width:104px">
    <div class="section__title">KITCHEN</div>
    <div class="section__text">Lorem ipsum dolor sit amet, consectetur adipiscing elit. Vivamus eu dui ex.</div>
  </div>
  <div class="page-bar"><span>© 2022 STANZA CHIARA, All rights reserved.</span><span class="page-bar__num">6</span></div>
</article>

<!-- balcony -->
<article class="slide col-a row-4">
  <div class="fill room-bg" style="left:160px;top:0;width:159px;height:179px" role="img" aria-label="Balcony interior, tinted in wine red"></div>
  <div class="photo photo--balcony1" style="left:8px;top:7px;width:179px;height:71px" role="img" aria-label="Terrace lounge with white sofa and ornamental grasses"></div>
  <div class="photo photo--balcony2" style="left:8px;top:85px;width:179px;height:71px" role="img" aria-label="Balcony with yellow sofa, floor lamp and black railing"></div>
  <div class="brand brand--mini" style="left:233px;top:36px">
    <svg width="26" height="26" viewBox="0 0 26 26"><circle cx="13" cy="13" r="12.5" fill="none" stroke="var(--rose)" stroke-width=".5" opacity=".8"/></svg>
    <div class="brand__name">Stanza<br>Chiara</div>
  </div>
  <div class="section__block" style="left:200px;top:99px;width:104px">
    <div class="section__title">BALCONY</div>
    <div class="section__text">Lorem ipsum dolor sit amet, consectetur adipiscing elit. Vivamus eu dui ex.</div>
  </div>
  <div class="page-bar"><span>© 2022 STANZA CHIARA, All rights reserved.</span><span class="page-bar__num">7</span></div>
</article>

<!-- contact -->
<article class="slide col-b row-4">
  <div class="fill room-bg" style="inset:0" role="img" aria-label="Bedroom with wooden beams, tinted in wine red"></div>
  <div class="cover__rule" style="left:100px;top:90px;width:50px"></div>
  <div class="brand brand--cover" style="top:48px">
    <svg width="44" height="44" viewBox="0 0 44 44"><circle cx="22" cy="22" r="21" fill="none" stroke="var(--rose)" stroke-width=".6"/></svg>
    <div class="brand__name">Stanza<br>Chiara</div>
  </div>
  <div class="contact__kicker">STANZA</div>
  <div class="contact__name">CHIARA</div>
  <div class="contact__address">DI MARTA DELFINI, VIA DEI TIGLI, 42</div>
  <ul class="contact__list">
    <li><svg viewBox="0 0 10 10"><path d="M2 1l2 2-1 1.3c.6 1.2 1.5 2.1 2.7 2.7L7 6l2 2-1.3 1.4C4.5 9 1 5.5.6 2.3z" fill="var(--rose)"/></svg>340/5551928</li>
    <li><svg viewBox="0 0 10 10"><circle cx="5" cy="5" r="2" fill="none" stroke="var(--rose)" stroke-width="1.1"/><path d="M7 3v3c0 1 1.8 1 1.8-1A3.8 3.8 0 1 0 7 8.3" fill="none" stroke="var(--rose)" stroke-width="1.1"/></svg>marta@stanzachiara.example</li>
    <li><svg viewBox="0 0 10 10"><circle cx="5" cy="5" r="4.3" fill="none" stroke="var(--rose)" stroke-width=".8"/><ellipse cx="5" cy="5" rx="1.8" ry="4.3" fill="none" stroke="var(--rose)" stroke-width=".8"/><path d="M.7 5h8.6" stroke="var(--rose)" stroke-width=".8"/></svg>www.stanzachiara.example</li>
  </ul>
  <div class="footer-band">© 2022 STANZA CHIARA, All rights reserved.</div>
</article>

</body>
</html>
```